Little Ones Can Soar
Brochure
onescansoar.org
I have a logo that was created by brand (business cards) mark maven and a web site that was designed by pixel sage, I am interested in intergrating those designs into two or tri fold business brochure. Your company has all the records that are needed
Corporate, businesses, retailers, Individuals and people of all walks of life. (prospects of give)
Need a brochure not expensive to print. What would be you suggestion as to the type of brochure needed?

```html
<!DOCTYPE html>
<html lang="en">
<head>
<meta charset="utf-8">
<title>Little Ones Can Soar – Brochure</title>
<link href="https://fonts.googleapis.com/css2?family=Open+Sans:wght@400;600;700&family=Arimo:wght@400;700&display=swap" rel="stylesheet">
<style>
:root{
  --paper:#ffffff;
  --ink:#1d1d1d;
  --blue:#1f4fa6;
  --blue-light:#4f7fd0;
  --orange:#f7941d;
  --green:#3a9b3a;
  --fold:#e4e4e4;
  --photo-a:#8fa9c9;
  --photo-b:#c9b48e;
}
*{margin:0;padding:0;box-sizing:border-box}
html,body{width:1200px;height:866px;overflow:hidden;background:var(--paper)}
.brochure{position:relative;width:1200px;height:866px;background:var(--paper);font-family:"Arimo",Arial,sans-serif;color:var(--ink)}
.rings{position:absolute;inset:0}
.panel{position:absolute;top:0;height:866px}
.panel-left{left:0;width:400px}
.panel-middle{left:400px;width:452px}
.panel-right{left:852px;width:348px}
.fold{position:absolute;top:0;width:1px;height:866px;background:var(--fold)}
.brand{position:absolute;left:60px;top:60px;width:290px;text-align:center}
.brand-mark{display:block;width:58px;height:58px;border-radius:50%;background:var(--orange);margin:0 auto 14px}
.brand-name{font-family:"Open Sans",sans-serif;font-weight:700;font-size:30px;color:var(--green);line-height:1.15}
.copy{font-size:13.2px;line-height:1.52;text-align:justify}
.copy p{margin-bottom:17px}
.panel-left .copy{position:absolute;left:29px;top:372px;width:355px}
.heading{font-family:"Open Sans",sans-serif;font-weight:400;font-size:24px;letter-spacing:.5px;text-transform:uppercase}
.heading-blue{color:var(--blue)}
.heading-orange{color:var(--orange)}
.volunteers{position:absolute;left:27px;top:40px}
.volunteers-copy{position:absolute;left:27px;top:105px;width:418px;text-align:left}
.volunteer-roles{color:var(--blue)}
.invitation{position:absolute;left:27px;top:418px}
.invitation-copy{position:absolute;left:27px;top:482px;width:418px;text-align:left}
.leadership{position:absolute;left:17px;top:40px}
.leader-copy{position:absolute;left:17px;top:100px;width:295px;text-align:left}
.leader-copy p{margin-bottom:14px}
.photo{position:absolute;left:852px;top:272px;width:320px;height:470px}
</style>
</head>
<body>
<main class="brochure">
  <svg class="rings" width="1200" height="866" viewBox="0 0 1200 866" aria-hidden="true">
    <defs>
      <linearGradient id="photoTone" x1="0" y1="0" x2="1" y2="1">
        <stop offset="0" stop-color="var(--photo-a)"/>
        <stop offset="1" stop-color="var(--photo-b)"/>
      </linearGradient>
    </defs>
    <circle cx="790" cy="470" r="300" fill="none" stroke="var(--orange)" stroke-width="42"/>
    <circle cx="1030" cy="505" r="335" fill="none" stroke="var(--blue)" stroke-width="34"/>
    <circle cx="1030" cy="505" r="300" fill="none" stroke="var(--blue-light)" stroke-width="10" opacity=".6"/>
  </svg>

  <div class="fold" style="left:400px"></div>
  <div class="fold" style="left:852px"></div>

  <svg class="photo" viewBox="0 0 320 470" role="img" aria-label="Photograph of a smiling child crawling out of a colourful play tunnel">
    <rect width="320" height="470" rx="8" fill="url(#photoTone)"/>
  </svg>

  <section class="panel panel-left">
    <div class="brand">
      <span class="brand-mark"></span>
      <span class="brand-name">Little Ones Can Soar</span>
    </div>
    <div class="copy">
      <p>Little Ones Can Soar Inc. mission is to enrich kids learning by providing the essential tools to succeed. The experiences the kids will have while participating in the company's programs will assist them in making their transition from grade level to grade level more smoothly. The resources will allow them to develop their skill sets that will be transferable in advanced grades.</p>
      <p>Kids should be taught how to communicate, speak and interact with peers appropriately. They should be provided various materials, games and activities to be motivated to learn in the areas of language, vocabulary, reading, mathematics, science, computers and social behaviors (discipline). Underserved kids need gifts of school supplies, backpacks, uniforms, and other essential tools to function in school.</p>
      <p>The kid demographic market has changed in the urban areas. Kids need help. Parents are losing their jobs and cannot provide for their kids basic educational necessities.</p>
    </div>
  </section>

  <section class="panel panel-middle">
    <h2 class="heading heading-blue volunteers">Volunteers</h2>
    <div class="copy volunteers-copy">
      <p>Please take this opportunity to get involved, by volunteering your talent and skills to a worthwhile cause.</p>
      <p>Volunteers are the fiber of our organization. If you are interested in becoming a volunteer and want to learn more about us, just forward us an e-mail.</p>
      <p class="volunteer-roles">Grant Writers "Little Ones Can Soar Inc."<br>Members Photographers</p>
    </div>
    <h2 class="heading heading-blue invitation">Invitation</h2>
    <div class="copy invitation-copy">
      <p>Little Ones Can Soar Inc. hopes that your company is interested in supporting our mission by enhancing the image of your company's community involvement.</p>
      <p>We would like companies to be part of our mission and be given an extended invitation.</p>
      <p>Corporate sponsorship raises awareness in the community. Bridge the gap in helping local kids by providing the essential tools to succeed and making our schools a better place to learn. Your support will yield an immediate return on your charitable contribution exposure for a title of the cost.</p>
    </div>
  </section>

  <section class="panel panel-right">
    <h2 class="heading heading-orange leadership">Leadership Team</h2>
    <div class="copy leader-copy">
      <p>Dana R. Holt<br>President &amp; CEO<br>LITTLE ONES CAN SOAR INC.</p>
      <p>Dana is the founder of the organization since its inception, a native of Jacksonville Fl. Dana was a territory manager for Carolina Leaf Company for nine years. Responsible for selling and maintaining a 4 million yr. territory in central New Jersey.</p>
      <p>Dana worked twenty two years as an operational assistant for Garden Line Transit. More</p>
    </div>
  </section>
</main>
</body>
</html>
```